Этикетка для Частная пивоварня " Корвенталь"
Опишите свою организацию или продукт и целевую аудиторию
Завод KORVENTAL построен и введен в эксплуатацию в 2015 году. Мы используем в процессе производства только натуральные ингредиенты высокого качества: немецкий хмель двух сортов и солод.
Целевая аудитория нашего пива- в основной массе мужчины.
Комментарии и пожелания для дизайнеров
Необходимо разработать концепт дизайна этикета на пиво « Тарвинское». Форма самой этикетки не принципиальна: может быть как прямоугольной, так и округлой формы. Главное требование-она должна гармонично сочетаться с формой бутылки.
Цветовая гамма для Тарвинского–готовы рассмотреть варианты: как сине-желто-белая, так и бежевая. Хотелось бы привлечь клиента узнаваемым дизайном пива «Тарвинское», ретро -стиль, но в то же время этикетка должна отличаться от представленных на рынке.
О производителе на этикетке будет говорить лишь фирменный логотип.
Обязательная информация на лицевую часть: « пиво светлое пастеризованное», « настоящее живое», « изготовлено из натуральных ингредиентов».
Контрэтикетка будет содержать текстовую часть( информация о составе, производителе, информацию для потребителя).
Планируем печать на льне. В качестве логотипа используется буква в обрамлении.

```html
<!DOCTYPE html>
<html lang="ru">
<head>
<meta charset="utf-8">
<title>Пиво Тарвинское — этикетка</title>
<link href="https://fonts.googleapis.com/css2?family=Oswald:wght@400;500;700&family=Marck+Script&display=swap" rel="stylesheet">
<style>
  :root {
    --page-bg: #ffffff;
    --label-dark: #17222c;
    --label-dark-2: #223140;
    --band-blue: #2f86c2;
    --band-blue-2: #3a95cf;
    --title-yellow: #f5c518;
    --title-shadow: #0b1117;
    --text-white: #f1ede4;
    --text-muted: #b9c0c6;
    --brand-red: #d8262b;
  }
  html, body {
    margin: 0;
    width: 1200px;
    height: 895px;
    overflow: hidden;
    background: var(--page-bg);
  }
  .canvas {
    position: relative;
    width: 1200px;
    height: 895px;
  }
  .label {
    position: absolute;
    left: 220px;
    top: 193px;
    width: 377px;
    height: 511px;
    overflow: hidden;
    background:
      radial-gradient(ellipse at 30% 20%, var(--label-dark-2) 0%, transparent 60%),
      radial-gradient(ellipse at 80% 70%, #1d2b38 0%, transparent 55%),
      var(--label-dark);
    color: var(--text-white);
    text-align: center;
  }
  .label__band {
    position: absolute;
    left: 0;
    right: 0;
    bottom: 0;
    height: 77px;
    background: linear-gradient(180deg, var(--band-blue-2), var(--band-blue));
  }
  .brand {
    position: absolute;
    top: 52px;
    left: 0;
    right: 0;
    display: flex;
    justify-content: center;
    align-items: center;
    gap: 7px;
    font-family: "Oswald", sans-serif;
    font-weight: 700;
    font-size: 15px;
    letter-spacing: 2px;
    color: var(--brand-red);
  }
  .brand__mark {
    width: 9px;
    height: 9px;
    background: var(--brand-red);
  }
  .product-kind {
    position: absolute;
    top: 140px;
    left: 0;
    right: 0;
    font-family: "Marck Script", cursive;
    font-size: 40px;
    line-height: 1;
    color: var(--text-white);
  }
  .product-name {
    position: absolute;
    top: 196px;
    left: 0;
    right: 0;
    margin: 0;
    font-family: "Oswald", sans-serif;
    font-weight: 700;
    font-size: 54px;
    line-height: 1;
    color: var(--title-yellow);
    text-shadow: 2px 3px 0 var(--title-shadow), 3px 4px 0 var(--title-shadow);
  }
  .spec-row {
    position: absolute;
    top: 285px;
    left: 0;
    right: 0;
    display: flex;
    justify-content: center;
    align-items: center;
    gap: 10px;
  }
  .spec-row__note {
    font-family: "Oswald", sans-serif;
    font-size: 6px;
    line-height: 1.1;
    color: var(--text-muted);
    text-align: left;
  }
  .spec-row__type {
    font-family: "Oswald", sans-serif;
    font-weight: 500;
    font-size: 15px;
    letter-spacing: 0.5px;
    color: var(--text-white);
  }
  .claim {
    position: absolute;
    top: 366px;
    left: 0;
    right: 0;
    font-family: "Oswald", sans-serif;
    font-weight: 500;
    font-size: 14px;
    letter-spacing: 1px;
    word-spacing: 6px;
    color: var(--text-white);
  }
  .ingredients {
    position: absolute;
    top: 389px;
    left: 0;
    right: 0;
    font-family: "Marck Script", cursive;
    font-size: 16px;
    color: var(--text-white);
  }
</style>
</head>
<body>
<main class="canvas">
  <section class="label">
    <div class="brand"><span class="brand__mark"></span>КОРВЕНТАЛЬ</div>
    <div class="product-kind">Пиво</div>
    <h1 class="product-name">ТАРВИНСКОЕ</h1>
    <div class="spec-row">
      <span class="spec-row__note">5,6%<br>АЛК</span>
      <span class="spec-row__type">СВЕТЛОЕ ПАСТЕРИЗОВАННОЕ</span>
      <span class="spec-row__note">500<br>МЛ</span>
    </div>
    <div class="claim">НАСТОЯЩЕЕ ЖИВОЕ</div>
    <div class="ingredients">Изготовлено из натуральных ингредиентов</div>
    <div class="label__band"></div>
  </section>
</main>
</body>
</html>
```